Structural Engineering Business Card

Veltrow Drafts does residential house plans for clients in Central Florida. Would like simple but elegant business card that is appropriate for a house plan engineering company. Prefer black business card with black/white them but open to other shades of blue. I uploaded a sample card that I came across that looked good but please come up with your own creative designs.

Contact Information for Business Card

Name, Title, Phone, Email, Address, website

```html
<!DOCTYPE html>
<html lang="en">
<head>
<meta charset="utf-8">
<title>Veltrow Drafts – Business Card</title>
<link href="https://fonts.googleapis.com/css2?family=Source+Sans+3:wght@400;700;800&display=swap" rel="stylesheet">
<style>
  :root {
    --backdrop: #e6e6e6;
    --card-blue: #065ba5;
    --art-light: #5b9ad3;
    --art-mid: #3a81c2;
    --art-soft: rgba(91, 154, 211, 0);
    --ink: #ffffff;
  }
  * { box-sizing: border-box; margin: 0; padding: 0; }
  html, body {
    width: 1200px; height: 960px; overflow: hidden;
    background: var(--backdrop);
    font-family: "Source Sans 3", "Source Sans Pro", sans-serif;
    color: var(--ink);
  }
  .card {
    position: absolute; left: 299px; width: 611px; height: 349px;
    background: var(--card-blue); overflow: hidden;
  }
  .card--front { top: 108px; }
  .card--back { top: 509px; }

  /* Front: house illustration area */
  .house-sketch {
    position: absolute; left: 0; top: 8px; width: 285px; height: 341px;
    background:
      linear-gradient(90deg, var(--art-mid) 0%, var(--art-light) 45%, var(--art-soft) 100%);
    clip-path: polygon(0 8%, 25% 0, 88% 22%, 95% 35%, 100% 70%, 95% 100%, 0 100%);
    opacity: .85;
  }
  .brand-name {
    position: absolute; font-weight: 800; color: var(--ink);
    letter-spacing: .5px; white-space: nowrap; line-height: 1;
  }
  .card--front .brand-name { left: 216px; top: 158px; font-size: 49px; }

  /* Back: floor plan area */
  .floor-plan {
    position: absolute; left: 385px; top: 0; width: 226px; height: 100%;
    background:
      linear-gradient(270deg, var(--art-light) 0%, var(--art-mid) 45%, var(--art-soft) 100%);
    clip-path: polygon(8% 0, 100% 0, 100% 100%, 30% 100%, 0 55%, 2% 20%);
    opacity: .85;
  }
  .card--back .brand-name {
    left: 32px; top: 296px; font-size: 38px;
    transform-origin: 0 0; transform: rotate(-90deg);
  }
  .contact-rail {
    position: absolute; left: 166px; top: 62px; width: 1.5px; height: 252px; background: var(--ink);
  }
  .contact-item { position: absolute; left: 136px; display: flex; align-items: flex-start; }
  .contact-item svg { width: 24px; height: 24px; flex: none; margin-right: 21px; }
  .contact-text { font-size: 15px; line-height: 22px; margin-top: 0; }
  .contact-text .holder-name { font-size: 18.5px; font-weight: 700; line-height: 23px; }
  .contact-text .holder-title { font-size: 15px; line-height: 20px; }
</style>
</head>
<body>

<section class="card card--front">
  <div class="house-sketch" role="img" aria-label="Line drawing of a modern two-storey house"></div>
  <div class="brand-name">Veltrow Drafts</div>
</section>

<section class="card card--back">
  <div class="floor-plan" role="img" aria-label="Architectural floor plan drawing"></div>
  <div class="brand-name">Veltrow Drafts</div>

  <div class="contact-rail"></div>

  <div class="contact-item" style="top:65px">
    <svg viewBox="0 0 24 24" fill="var(--card-blue)" stroke="#fff" stroke-width="1.3"><circle cx="12" cy="12" r="10.5"/><circle cx="12" cy="9.5" r="3"/><path d="M6.5 17.5c1-2.8 3-4 5.5-4s4.5 1.2 5.5 4" fill="none"/></svg>
    <div class="contact-text"><p class="holder-name">Daniel Marsh</p><p class="holder-title">Architectural Director</p></div>
  </div>

  <div class="contact-item" style="top:176px">
    <svg viewBox="0 0 24 24" fill="var(--card-blue)" stroke="#fff" stroke-width="1.3"><circle cx="12" cy="12" r="10.5"/><path d="M12 18s-4-4.3-4-7.3a4 4 0 0 1 8 0c0 3-4 7.3-4 7.3z" fill="none"/><circle cx="12" cy="10.6" r="1.4" fill="none"/></svg>
    <p class="contact-text">418 Cedar Point Lane, Suite 210<br>Lakewood, FL 32801</p>
  </div>

  <div class="contact-item" style="top:228px">
    <svg viewBox="0 0 24 24" fill="var(--card-blue)" stroke="#fff" stroke-width="1.3"><circle cx="12" cy="12" r="10.5"/><path d="M8.5 7l2 2.3-1 1.4c.8 1.6 2 2.8 3.6 3.6l1.4-1 2.3 2-1.2 1.5c-3.8-.4-7.2-3.8-7.6-7.6z" fill="none"/></svg>
    <p class="contact-text">407-555-0143</p>
  </div>

  <div class="contact-item" style="top:256px">
    <svg viewBox="0 0 24 24" fill="var(--card-blue)" stroke="#fff" stroke-width="1.3"><circle cx="12" cy="12" r="10.5"/><rect x="7" y="8.5" width="10" height="7" fill="none"/><path d="M7 8.5l5 4 5-4" fill="none"/></svg>
    <p class="contact-text">daniel@veltrowdrafts.com</p>
  </div>

  <div class="contact-item" style="top:283px">
    <svg viewBox="0 0 24 24" fill="var(--card-blue)" stroke="#fff" stroke-width="1.3"><circle cx="12" cy="12" r="10.5"/><circle cx="12" cy="12" r="5.5" fill="none"/><path d="M6.5 12h11M12 6.5c-2.2 3-2.2 8 0 11M12 6.5c2.2 3 2.2 8 0 11" fill="none"/></svg>
    <p class="contact-text">www.veltrowdrafts.com</p>
  </div>
</section>

</body>
</html>
```